Tobin's Jewelry Studio Needs a Moving Location Flyer

We need a flyer to inform our customers of our location moving. We will be moving to our city's downtown which is only 1 mile away from our current address. We will be having a moving sale ( Up to 80% off). The sale starts Sept. 8th Our business creates, sells, and repairs fine jewelry. Dimensions are 5"x8"

Target Market(s)

Women ages 25-55

Industry/Entity Type

Jewelry

Colors
85abd2
cfdeed

Requirements
Must have
• Our logo
• Mention of the sale
• Our current address
• 4187 Marsh Creek Blvd.
• Brookhollow, Ca 91642
• (909)417-2863
Nice to have
• Mention that we're relocating to downtown Brookhollow (new location opening Nov. 1st.)

```html
<!DOCTYPE html>
<html lang="en">
<head>
<meta charset="utf-8">
<title>Tobin's Jewelry Studio – Moving Sale Flyer</title>
<link href="https://fonts.googleapis.com/css2?family=Oswald:wght@500;700&family=Roboto+Condensed:wght@300;400&display=swap" rel="stylesheet">
<style>
  :root {
    --page-bg: #e9edf2;
    --brand-blue: #85abd2;
    --brand-blue-deep: #6f97c8;
    --brand-pale: #cfdeed;
    --shield-top: #3f4f96;
    --shield-bottom: #8aa6d6;
    --navy: #2a2f78;
    --ink: #1f1f24;
    --white: #ffffff;
  }
  * { margin: 0; padding: 0; box-sizing: border-box; }
  html, body { width: 1200px; height: 1200px; overflow: hidden; }
  body { background: var(--page-bg); position: relative; font-family: "Roboto Condensed", sans-serif; }

  .flyer {
    position: absolute; left: 260px; top: 56px; width: 680px; height: 1088px;
    overflow: hidden; box-shadow: 0 6px 24px rgba(0,0,0,.18);
    background: var(--white);
  }
  .flyer__pattern {
    position: absolute; inset: 0;
    background: radial-gradient(ellipse at 50% 45%, #f4f7fb 0%, #dce7f3 55%, #c8d9ec 100%);
  }
  .flyer__cap { position: absolute; left: 0; top: 0; width: 680px; height: 170px; }

  .brand {
    position: absolute; top: 66px; left: 0; width: 100%;
    display: flex; justify-content: center; align-items: center; gap: 12px;
  }
  .brand__dot { width: 40px; height: 40px; border-radius: 50%; background: var(--brand-pale); }
  .brand__name { font-family: "Roboto Condensed", sans-serif; font-weight: 400; font-size: 24px; color: var(--navy); }

  .center { position: absolute; left: 0; width: 100%; text-align: center; line-height: 1; }
  .headline {
    font-family: "Oswald", sans-serif; font-weight: 700; color: var(--brand-blue-deep);
    text-transform: uppercase; letter-spacing: .5px;
  }
  .headline--one { top: 190px; font-size: 64px; }
  .headline--two { top: 258px; font-size: 64px; }
  .distance { top: 345px; font-size: 50px; color: var(--ink); font-weight: 300; }
  .distance-sub { top: 412px; font-size: 30px; color: var(--ink); font-weight: 300; }

  .address {
    position: absolute; left: 90px; top: 452px; width: 500px; height: 76px;
    border-radius: 16px; background: var(--brand-blue);
    color: var(--white); font-size: 25px; font-weight: 300; font-style: normal;
    text-align: center; line-height: 32px; padding-top: 6px; white-space: nowrap;
  }

  .shield { position: absolute; left: 190px; top: 562px; width: 300px; height: 316px; }
  .shield__text { position: absolute; left: 190px; top: 562px; width: 300px; text-align: center; }
  .shield__title { margin-top: 14px; font-family: "Oswald", sans-serif; font-weight: 500; font-size: 44px; color: var(--brand-pale); line-height: 1.1; }
  .shield__upto { font-size: 46px; color: var(--white); font-weight: 300; line-height: 1; }
  .shield__value {
    font-family: "Oswald", sans-serif; font-weight: 700; font-size: 104px; line-height: 1;
    color: var(--white); -webkit-text-stroke: 3px var(--navy); paint-order: stroke fill;
  }
  .shield__off { font-size: 58px; color: var(--white); font-weight: 300; line-height: .9; }

  .sale-date { top: 918px; font-family: "Oswald", sans-serif; font-weight: 500; font-size: 46px; color: var(--ink); }
  .sale-date__day { font-size: 58px; }

  .tagline {
    position: absolute; left: 44px; top: 1008px; width: 593px; height: 42px;
    background: var(--brand-blue); color: var(--navy);
    font-size: 27px; font-weight: 300; text-align: center; line-height: 42px; white-space: nowrap;
  }
</style>
</head>
<body>
  <main class="flyer">
    <div class="flyer__pattern" role="img" aria-label="Soft pale blue background with swirling curved arrow pattern"></div>

    <svg class="flyer__cap" viewBox="0 0 680 170" aria-hidden="true">
      <path d="M0 0 H680 V0 C600 110 460 160 340 160 C220 160 80 110 0 0 Z" fill="var(--white)"/>
      <path d="M0 0 C80 110 220 160 340 160 C460 160 600 110 680 0" fill="none" stroke="var(--brand-blue-deep)" stroke-width="5"/>
    </svg>

    <div class="brand">
      <span class="brand__dot"></span>
      <span class="brand__name">Tobin's Jewelry Studio</span>
    </div>

    <h1 class="center headline headline--one">We Will Be</h1>
    <h1 class="center headline headline--two">Moving To Our City's</h1>
    <p class="center distance">Only 1 mile away</p>
    <p class="center distance-sub">From Our Current Address</p>

    <address class="address">4187 Marsh Creek Blvd. Brookhollow, Ca 91642<br>- (909)417-2863</address>

    <svg class="shield" viewBox="0 0 300 316" aria-hidden="true">
      <defs>
        <linearGradient id="shieldFill" x1="0" y1="0" x2="0" y2="1">
          <stop offset="0" stop-color="var(--shield-top)"/>
          <stop offset="1" stop-color="var(--shield-bottom)"/>
        </linearGradient>
      </defs>
      <path d="M8 6 H292 V240 Q292 262 270 272 L150 314 L30 272 Q8 262 8 240 Z" fill="var(--white)"/>
      <path d="M14 6 H286 V236 Q286 256 266 265 L150 306 L34 265 Q14 256 14 236 Z" fill="url(#shieldFill)"/>
      <rect x="0" y="0" width="300" height="6" fill="var(--navy)"/>
    </svg>
    <div class="shield__text">
      <p class="shield__title">Moving Sale</p>
      <p class="shield__upto">Up to</p>
      <p class="shield__value">80%</p>
      <p class="shield__off">off</p>
    </div>

    <p class="center sale-date">Sale starts <span class="sale-date__day">8</span>th Sept.</p>

    <p class="tagline">Our Business Creates, Sells, And Repairs Fine Jewelry.</p>
  </main>
</body>
</html>
```